Business Card needed for International Migration and Education business

we are based in Australia, the business is called 'Brightpath Migration' and its sister business for international education is called 'Brightpath Studies' - we need the design for the business 'Brightpath Migration' - Brightpath Migration is about migration to Australia (but not limited to Australia only therefore purely Australian look would not fit). We would like to see designs that use the color blue or acqua and maybe orange..all those colours don't have to be used together and not only those colours are to be used. We are looking for a modern design. The final design should communicate modern thinking, professionalism, dynamism, confidence. We would like to use the same business card design for our sister business "Brightpath Studies" - which is business about studying in different countries as we recruit students to study in Australia, USA, New Zealand, Canada, UK etc. We would like to be able the final design to be easily changed by us to fit the 'Brightpath Studies' business - we would only change the contact text (email address etc)

The information to be included in the business card: Rosalind Tepperly Managing Director Migration Agent MARN 0719264 Brightpath Migration postal address: PO Box 2274, Fernvale South VIC 3195, Australia mobile: 0417296385 office address: Level 1, 287 Corran Street, Tullagrove VIC 3211 web www.brightpathmigration.example telephone: 61 3 8574 3162 fax + 61 3 8539 7041 email: rosalind@brightpathmigration.example

Industry/Entity Type

Education

```html
<!DOCTYPE html>
<html lang="en">
<head>
<meta charset="utf-8">
<title>Brightpath Migration – Business Card</title>
<link rel="stylesheet" href="https://fonts.googleapis.com/css2?family=Open+Sans:wght@400;600&display=swap">
<style>
  :root {
    --page-bg: #ffffff;
    --card-dark: #0b0c0e;
    --card-mid: #1c1e22;
    --aqua: #2fb2e0;
    --silver: #d4d8dc;
    --text-light: #d7d9dc;
    --text-muted: #b9bcc0;
    --rule-light: #e6e8ea;
    --rule-dark: #5c6066;
  }
  * { box-sizing: border-box; margin: 0; padding: 0; }
  html, body {
    width: 1200px;
    height: 900px;
    overflow: hidden;
    background: var(--page-bg);
    font-family: "Open Sans", Arial, sans-serif;
  }
  .canvas {
    position: relative;
    width: 1200px;
    height: 900px;
  }
  .card {
    position: absolute;
    left: 160px;
    top: 185px;
    width: 880px;
    height: 530px;
    border-radius: 30px;
    overflow: hidden;
    background:
      radial-gradient(ellipse at 55% 42%, var(--card-mid) 0%, var(--card-dark) 70%);
    box-shadow: 0 18px 40px rgba(0,0,0,0.22);
  }
  .brand {
    position: absolute;
    left: 62px;
    top: 160px;
    display: flex;
    align-items: center;
    gap: 24px;
  }
  .brand-circle {
    width: 110px;
    height: 110px;
    border-radius: 50%;
    border: 10px solid var(--aqua);
  }
  .brand-name {
    font-weight: 600;
    font-size: 40px;
    line-height: 1.1;
    color: var(--silver);
  }
  .person {
    position: absolute;
    right: 54px;
    top: 44px;
    text-align: right;
  }
  .person-name {
    font-weight: 600;
    font-size: 27px;
    line-height: 36px;
    color: var(--aqua);
  }
  .person-title {
    font-size: 18px;
    line-height: 25px;
    color: var(--text-muted);
  }
  .divider {
    position: absolute;
    left: 0;
    right: 0;
    top: 298px;
    height: 4px;
    background: linear-gradient(90deg, var(--rule-dark), var(--rule-light) 60%, var(--rule-dark));
  }
  .contacts {
    position: absolute;
    left: 62px;
    top: 318px;
    list-style: none;
  }
  .contacts li {
    display: flex;
    align-items: center;
    gap: 12px;
    font-size: 20px;
    line-height: 27px;
    color: var(--text-light);
  }
  .contacts svg {
    width: 20px;
    height: 20px;
    flex: none;
    fill: var(--aqua);
  }
</style>
</head>
<body>
<div class="canvas">
  <div class="card">
    <div class="person">
      <div class="person-name">Rosalind Tepperly</div>
      <div class="person-title">Managing Director</div>
      <div class="person-title">Migration Agent</div>
      <div class="person-title">MARN 0719264</div>
    </div>

    <div class="brand">
      <div class="brand-circle"></div>
      <div class="brand-name">Brightpath Migration</div>
    </div>

    <div class="divider"></div>

    <ul class="contacts">
      <li>
        <svg viewBox="0 0 20 20" aria-hidden="true"><path d="M5 1h10a1 1 0 0 1 1 1v16a1 1 0 0 1-1 1H5a1 1 0 0 1-1-1V2a1 1 0 0 1 1-1zm1 2v9h8V3zm1 11v1.5h1.5V14zm3 0v1.5h1.5V14zm3 0v1.5h1.5V14z"/></svg>
        0417296385
      </li>
      <li>
        <svg viewBox="0 0 20 20" aria-hidden="true"><path d="M4 1.5l3 .5 1.5 4-2 1.5a11 11 0 0 0 6 6l1.5-2 4 1.5.5 3c-1 1.5-2.5 2-4 1.8C8 17 3 12 2.2 5.5 2 4 2.5 2.5 4 1.5z"/></svg>
        61 3 8574 3162
      </li>
      <li>
        <svg viewBox="0 0 20 20" aria-hidden="true"><path d="M5 2h8l2 2v4H5zM2 9h16a1 1 0 0 1 1 1v7a1 1 0 0 1-1 1H2a1 1 0 0 1-1-1v-7a1 1 0 0 1 1-1zm2 3v2h6v-2zm9 0v1.5h1.5V12zm0 3v1.5h1.5V15z"/></svg>
        + 61 3 8539 7041
      </li>
      <li>
        <svg viewBox="0 0 20 20" aria-hidden="true"><path d="M10 1.5l9 8-1.3 1.4L16 9.4V18h-4.5v-5h-3v5H4V9.4l-1.7 1.5L1 9.5z"/></svg>
        PO Box 2274, Fernvale South VIC 3195, Australia
      </li>
      <li>
        <svg viewBox="0 0 20 20" aria-hidden="true"><path d="M10 1a6.5 6.5 0 0 1 6.5 6.5C16.5 12 10 19 10 19S3.5 12 3.5 7.5A6.5 6.5 0 0 1 10 1zm0 4a2.5 2.5 0 1 0 0 5 2.5 2.5 0 0 0 0-5z"/></svg>
        Level 1, 287 Corran Street, Tullagrove VIC 3211
      </li>
      <li>
        <svg viewBox="0 0 20 20" aria-hidden="true"><path d="M10 1a9 9 0 1 1 0 18 9 9 0 0 1 0-18zm-1 2.1C7.7 4.6 7 6.6 6.9 9H9zm2 0V9h2.1c-.1-2.4-.8-4.4-2.1-5.9zM4.9 9c.1-2 .6-3.7 1.5-5A7 7 0 0 0 3.1 9zm10.2 0h1.8a7 7 0 0 0-3.3-5c.9 1.3 1.4 3 1.5 5zM3.1 11a7 7 0 0 0 3.3 5c-.9-1.3-1.4-3-1.5-5zm3.8 0c.1 2.4.8 4.4 2.1 5.9V11zm4.1 0v5.9c1.3-1.5 2-3.5 2.1-5.9zm4.1 0c-.1 2-.6 3.7-1.5 5a7 7 0 0 0 3.3-5z"/></svg>
        www.brightpathmigration.example
      </li>
      <li>
        <svg viewBox="0 0 20 20" aria-hidden="true"><path d="M1 5l9 6 9-6v11a1 1 0 0 1-1 1H2a1 1 0 0 1-1-1zm1-2h16l-8 5.5z"/></svg>
        rosalind@brightpathmigration.example
      </li>
    </ul>
  </div>
</div>
</body>
</html>
```